Organic Sunscreen Business "VelloraPure" Needs Package Design

Our company VelloraPure, manufactures an anti-ageing SPF 15 sunscreen product.

We specialise in the world's most rare and luxury organic anti-ageing ingredients.

We require an attractive package design for a 2.5 oz/75 ml squeezy bottle with box design, a few examples of similar examples which we like are attached.

We have a logo, barcode and graphic, which has been uploaded, and the bottle is to convey the message of wealth and luxury as well as organic sunscreen, we would prefer the package to be colourful and creative in order to sell.

I have included 2 rough sketches of the basic elements and layout of the design. And the box is to be similar to the bottle but to contain an extra caption.

Also, the sketch is only for a guide on how I would like the package, i.e. the labels and graphics can be in different positions/layouts thanks. And any additional creative images, text or fonts would be considered.

Industry/Entity Type

Business

Requirements
Must have
• FRONT of Bottle:
• LABEL 1: Logo (attached)
• LABEL 2:
• SPF 15
• Non-Nano
• Technology
• 100% Organic
• Paraben Free
• LABEL 3: (Larger/higher emphasis than Label 2)
• Anti-Ageing
• Moisturiser
• BACK of Bottle:
• Introduction: (For me to add personally at later date)
• Warnings: For external use only. Do not use on damaged or broken skin. Stop use and ask a doctor if rash occurs. When using this product keep out of eyes. Rinse with water to remove.
• Directions: Shake well before use. Apply liberally 15 minutes before sun exposure. Use a water resistant sunscreen if swimming or sweating. Reapply at least every 2 hours. Children under 6 months: Ask a doctor.
• Active Ingredient: Non-Nano Zinc Oxide (6%)
• Also contains: (For me to add personally at later date)
• Barcode: (image attached)
• Contact: www.vellorapure-example.com.au
• 2.5oz/7ml e
• BOX:
• Same as bottle, but one side will contain the caption:
• "7 NATURAL WONDERS IN 1" (In a creative style)
Nice to have
• Additional Text/Images/Fonts relating to the subject(s)
• Most creative design will be the winner.

```html
<!DOCTYPE html>
<html lang="en">
<head>
<meta charset="utf-8">
<title>VelloraPure Tube Labels</title>
<link href="https://fonts.googleapis.com/css2?family=Cinzel:wght@400&family=Arimo:wght@400&display=swap" rel="stylesheet">
<style>
:root{
  --gold:#cdb27e;
  --gold-text:#c99a45;
  --gold-soft:#e6d3a6;
  --label-white:#ffffff;
  --stage:#f1f1f1;
  --brand-ink:#1f1f1f;
  --edge:#dcdcdc;
}
*{margin:0;padding:0;box-sizing:border-box}
html,body{width:1200px;height:980px;overflow:hidden}
body{background:var(--stage);position:relative;font-family:'Arimo',Arial,sans-serif}
.label{position:absolute;top:70px;height:705px;background:var(--label-white);border:1px solid var(--edge);overflow:hidden}
.label--organic{left:125px;width:330px}
.label--spf{left:470px;width:330px}
.label--moisturiser{left:815px;width:333px}
.abs{position:absolute;left:0;right:0;text-align:center}
.brand{font-family:'Cinzel',serif;font-weight:400;font-size:21px;color:var(--brand-ink);letter-spacing:.5px}
.brand-mark{position:absolute;left:50%;width:70px;height:70px;margin-left:-35px;border-radius:50%;background:var(--gold)}
.band{position:absolute;left:0;right:0;background:var(--gold)}
.claim{color:var(--gold-text);font-size:14px;line-height:1.05;letter-spacing:.2px}
.claim--big{font-size:17px}
.volume{color:var(--gold-text);font-size:11px;line-height:1}
.volume small{display:block;font-size:8px}
.ornament{position:absolute;left:50%;width:62px;height:40px;margin-left:-31px;border-radius:6px;background:var(--gold-soft);opacity:.7}
.top-cap{position:absolute;left:0;right:0;top:0;height:152px;background:var(--gold)}
.logo-dome{position:absolute;left:50%;top:85px;width:130px;height:130px;margin-left:-65px;border-radius:50%;background:var(--label-white)}
</style>
</head>
<body>

<section class="label label--organic">
  <div class="brand-mark" style="top:108px"></div>
  <div class="abs brand" style="top:192px">VelloraPure</div>
  <div class="band" style="top:230px;height:12px"></div>
  <div class="band" style="top:250px;height:96px"></div>
  <div class="abs claim" style="top:422px">100%<br>ORGANIC</div>
  <div class="abs claim" style="top:472px">PARABEN FREE</div>
  <div class="abs volume" style="top:620px">75<small>ML</small></div>
  <div class="ornament" style="top:630px" role="img" aria-label="Gold fleur-de-lis ornament"></div>
</section>

<section class="label label--spf">
  <div class="abs claim claim--big" style="top:172px"><span style="font-size:13px">SFP</span> 15</div>
  <div class="abs claim" style="top:205px">NON-NANO<br>TECHNOLOGY</div>
  <div class="brand-mark" style="top:405px"></div>
  <div class="abs brand" style="top:494px">VelloraPure</div>
  <div class="band" style="top:587px;height:8px"></div>
  <div class="band" style="top:603px;height:102px"></div>
  <div class="abs volume" style="top:620px;color:var(--label-white)">75<small>ML</small></div>
  <div class="ornament" style="top:630px;background:var(--label-white);opacity:.45" role="img" aria-label="White fleur-de-lis ornament"></div>
</section>

<section class="label label--moisturiser">
  <div class="top-cap"></div>
  <div class="band" style="top:162px;height:10px"></div>
  <div class="logo-dome"></div>
  <div class="brand-mark" style="top:112px"></div>
  <div class="abs brand" style="top:202px">VelloraPure</div>
  <div class="abs claim claim--big" style="top:362px">7<span style="font-size:12px"> IN </span>1<span style="font-size:15px"> EXTREME</span></div>
  <div class="abs claim" style="top:395px">ANTI-AGEING<br>MOISTURISER</div>
  <div class="abs volume" style="top:620px">75<small>ML</small></div>
  <div class="ornament" style="top:630px" role="img" aria-label="Gold fleur-de-lis ornament"></div>
</section>

</body>
</html>
```